Hardcore nerd needs to stand out in a sea of dull Defence business cards

Wombat Devices is a new Australian consulting engineering company that turns research and theory into practical systems. No evangelistic fluff, just mathematics and physics into electronic and optical circuits for consumer products, scientific research or Defence applications.

We already have a recognised logo (provided) which is often dark blue/black on a light background but we're open to other combinations. (Us engineers tend to have limited aesthetic imagination :)

Some of our recent products have included:
* Instrumentation for electrical testing,
* Radar jammers,
* GPS antenna design,
* Satellite tracking systems,
* High power lasers

We're open to both single and double-sided designs - happy to be convinced either way.

P.S. Another group is working on the web page, so - alas - our web site is currently of no use for images/ideas...

Target Market(s)

Engineering managers,
Scientists

Contact Information for Business Card

Dr Colin Marsh
R&D Engineer

colin@wombatdevicesco.com.au
0427 563 210

PO Box XXX (to be confirmed)
Banks ACT 2913
Australia

Font styles to use
Serif
Sans Serif

Colors

Designer to choose colors to be used in the design.

Requirements
Must have
• My contact details!
• I've had many (great) "bold and plain" designs submitted already, so feel free to be artistically creative :)
• Happy to take advice re fonts/colours/printability etc.
Nice to have
• I'm not sure if "lists" are more at home on a CV than a business card, but representative services include:
• Applied electromagnetics
• RF and high speed electronics
• Signal and image processing
• Electro-optical and laser systems
• Concept-to-prototype design services
• If you're considering double sided cards, then often measuring/alignment grids/rulers feature on the back of similar cards.
• e.g. https://www.lumoptix-example.com/newgrouppage9.cfm?objectgroup_id=4815
• https://www.lumoptix-example.com/newgrouppage9.cfm?objectgroup_ID=4817
• ..or even a "Smith chart" (google will return lots)
• Generic images to represent a capability might work - googling images associated with keyword for each of these areas might help:
• - "passive radar", "phased array", "fdtd", "vircator"
• RF and high speed electronic design
• - "smith chart", "microstrip circuits", "dimensioned drawing", "electronic schematic"
• - "dft", "iir filter"
• - "optical cavity". "laser energy level diagram"
• Background/watermarked images outlines/wireframes/schematics would probably look OK.
Should not have
• If a list of projects/services is provided, it is important not to make the client feel that this is "all" the company can do. Engineering design is a creative discipline (like graphics :)
• Please, no stock "military" snaps like planes, missiles, etc!

```html
<!DOCTYPE html>
<html lang="en">
<head>
<meta charset="utf-8">
<title>Wombat Devices – Business Card</title>
<link href="https://fonts.googleapis.com/css2?family=Lato:wght@400;700;900&display=swap" rel="stylesheet">
<style>
  :root {
    --backdrop: #e7e4e0;
    --card-dark: #2a292a;
    --card-dark-deep: #1f1e1f;
    --card-light: #ffffff;
    --navy: #1e2a6b;
    --watermark: #343334;
    --ink-light: #ffffff;
  }
  html, body {
    margin: 0;
    width: 1200px;
    height: 900px;
    overflow: hidden;
    background: var(--backdrop);
  }
  .stage {
    position: relative;
    width: 1200px;
    height: 900px;
  }
  .card {
    position: absolute;
    left: 260px;
    width: 680px;
    height: 388px;
    border-radius: 22px;
    overflow: hidden;
    box-shadow: 0 14px 30px rgba(0,0,0,0.25);
  }
  .card--back { top: 46px; background: var(--card-dark); }
  .card--front { top: 466px; background: var(--card-light); }
  .card svg { display: block; width: 680px; height: 388px; }
  .wordmark { font-family: "Lato", sans-serif; font-weight: 900; letter-spacing: 1px; }
  .wordmark--light { fill: var(--ink-light); }
  .wordmark--navy { fill: var(--navy); }
  .service { font-family: "Lato", sans-serif; font-weight: 700; font-size: 20px; fill: var(--ink-light); }
  .contact-name { font-family: "Lato", sans-serif; font-weight: 900; font-size: 29px; fill: var(--ink-light); }
  .contact-line { font-family: "Lato", sans-serif; font-weight: 400; font-size: 20px; fill: var(--ink-light); }
</style>
</head>
<body>
<div class="stage">

  <!-- Back side -->
  <section class="card card--back" aria-label="Card back with services">
    <svg viewBox="0 0 680 388" xmlns="http://www.w3.org/2000/svg">
      <circle class="watermark-disc" cx="370" cy="200" r="110" fill="var(--watermark)"/>
      <circle cx="52" cy="56" r="22" fill="var(--ink-light)"/>
      <text class="wordmark wordmark--light" x="86" y="67" font-size="30">WOMBAT DEVICES</text>

      <g class="service-list" text-anchor="end">
        <text class="service" x="622" y="236">Radar jammers</text>
        <text class="service" x="622" y="266">High power lasers</text>
        <text class="service" x="622" y="296">GPS antenna design</text>
        <text class="service" x="622" y="326">Satellite tracking systems</text>
        <text class="service" x="622" y="356">Instrumentation for electrical testing</text>
      </g>
      <g class="service-bullets" fill="var(--ink-light)">
        <circle cx="642" cy="229" r="7"/>
        <circle cx="642" cy="259" r="7"/>
        <circle cx="642" cy="289" r="7"/>
        <circle cx="642" cy="319" r="7"/>
        <circle cx="642" cy="349" r="7"/>
      </g>
    </svg>
  </section>

  <!-- Front side -->
  <section class="card card--front" aria-label="Card front with contact details">
    <svg viewBox="0 0 680 388" xmlns="http://www.w3.org/2000/svg">
      <defs>
        <linearGradient id="dark-panel" x1="0" y1="0" x2="1" y2="1">
          <stop offset="0" stop-color="var(--card-dark)"/>
          <stop offset="1" stop-color="var(--card-dark-deep)"/>
        </linearGradient>
      </defs>
      <g class="swoosh">
        <path transform="translate(20,-14)" fill="var(--navy)"
              d="M-40,80 C150,30 330,40 390,150 C430,230 440,330 560,388 L-40,430 Z"/>
        <path transform="translate(9,-7)" fill="var(--card-light)"
              d="M-40,80 C150,30 330,40 390,150 C430,230 440,330 560,388 L-40,430 Z"/>
        <path fill="url(#dark-panel)"
              d="M-40,80 C150,30 330,40 390,150 C430,230 440,330 560,388 L-40,430 Z"/>
      </g>

      <g class="contact">
        <text class="contact-name" x="42" y="138">Dr Colin Marsh</text>
        <text class="contact-line" x="42" y="166">R&amp;D Engineer</text>
        <text class="contact-line" x="42" y="206">PO Box XXX</text>
        <text class="contact-line" x="42" y="232">Banks ACT 2913, Australia</text>

        <g class="icon-phone" fill="none" stroke="var(--ink-light)" stroke-width="2">
          <circle cx="52" cy="266" r="10"/>
          <path d="M47,262 q0,8 10,9" stroke-linecap="round"/>
        </g>
        <text class="contact-line" x="72" y="273">0427 563 210</text>

        <g class="icon-mail" fill="none" stroke="var(--ink-light)" stroke-width="2">
          <circle cx="52" cy="300" r="10"/>
          <rect x="46" y="296" width="12" height="8"/>
          <path d="M46,296 l6,4 l6,-4"/>
        </g>
        <text class="contact-line" x="72" y="307">colin@wombatdevicesco.com.au</text>
      </g>

      <g class="brand">
        <circle cx="596" cy="186" r="34" fill="var(--navy)"/>
        <text class="wordmark wordmark--navy" x="640" y="262" font-size="30" text-anchor="end">WOMBAT</text>
        <text class="wordmark wordmark--navy" x="640" y="296" font-size="30" text-anchor="end">DEVICES</text>
      </g>
    </svg>
  </section>

</div>
</body>
</html>
```